Nordic Joinery Guild Wordpress Theme and newsletter template

We at the NJG are looking to start a Wordpress website and also send out a newsletter (web). We have just completed a Logo design project with ArtFlockly and we were so pleased with the results that we would like to see what the designers can come up with for a Wordpress theme and a template for an online newsletter. The theme has to support Icelandic letters. It also has to have a subscription option by email. We would need to have the option to add advertisement banners. The theme has to be easy to work with.
Below we have added a two websites for a example of what we are looking for: .
http://www.torvexhub.example/
http://www.brakkel.example/
The newsletter has to have a similar theme as the website and will be used with MS Publisher.

Attached is the new NJG logo.
Updates

Project Deadline Extended Reason: Not fully happy with the designs we have gotten so far. Would like to extend time to see if improvements can be made. Added Tuesday, June 16, 2015

Target Market(s)

Welding association members, welding and metalworking industry, suppliers in welding industry, International welding community, other national welding associations, welding education community

Industry/Entity Type

Welding

Number of Pages Required

3 page

Requirements
Must have
• The TKBÓ logo
• Icelandic letters
• email formpage
• Advertisement space/banners/buttons
• Easy to manage
• Compatible with Wordpress
Nice to have
• Welding pictures
• Nice graphics
Should not have
• Should not be dark and heavy set.

```html
<!DOCTYPE html>
<html lang="en">
<head>
<meta charset="utf-8">
<title>TKBÓ – Trésmiðjufélag Kjalar</title>
<link href="https://fonts.googleapis.com/css2?family=Russo+One&family=Yanone+Kaffeesatz:wght@500&family=Arimo:wght@400;700&display=swap" rel="stylesheet">
<style>
:root{
  --brand-red:#d42b2f;
  --brand-blue:#0b8cc6;
  --deep-blue:#175a78;
  --button-blue:#116d98;
  --page-bg:#f4f4f4;
  --text:#444;
  --heading:#3b3b3b;
  --navy:#17365d;
  --white:#fff;
}
html,body{margin:0;padding:0;overflow:hidden;}
body{background:var(--page-bg);font-family:Arimo,Arial,sans-serif;color:var(--text);}
.page{position:relative;width:974px;height:1200px;overflow:hidden;background:var(--page-bg);}
.abs{position:absolute;}

.hero{left:0;top:0;width:974px;height:485px;
  background:radial-gradient(ellipse at 58% 68%,#e6f2ff 0,#8fb6d9 6%,#3d5f86 20%,transparent 42%),
             radial-gradient(ellipse at 80% 55%,#c9782f 0,transparent 38%),
             linear-gradient(160deg,#6f7f95 0%,#2c3d58 45%,#1f2533 75%,#3a2a22 100%);}
.hero-title{left:82px;top:176px;font-family:"Russo One",sans-serif;font-size:30px;color:var(--brand-red);margin:0;white-space:nowrap;}
.hero-sub{left:83px;top:222px;font-size:19px;color:var(--white);margin:0;white-space:nowrap;}

.header{left:83px;top:0;width:808px;height:102px;background:rgba(238,240,242,.96);border-radius:0 0 8px 8px;}
.logo{left:100px;top:30px;display:flex;align-items:center;gap:8px;font-family:Arimo,sans-serif;font-weight:700;font-size:30px;color:var(--brand-blue);}
.logo-dot{width:16px;height:16px;border-radius:50%;background:var(--brand-red);}
.call{left:432px;top:19px;display:flex;align-items:center;gap:8px;font-family:"Yanone Kaffeesatz",sans-serif;font-size:22px;color:#333;white-space:nowrap;}
.search{left:648px;top:19px;display:flex;}
.search-field{width:175px;height:27px;box-sizing:border-box;border:1px solid #ccc;background:var(--white);font-size:11px;color:#777;padding:7px 8px;}
.search-go{width:35px;height:27px;background:var(--brand-red);color:var(--white);font-size:11px;font-weight:700;text-align:center;line-height:27px;}
.nav{left:362px;top:64px;width:529px;height:38px;background:var(--brand-blue);border-radius:4px 0 6px 0;}
.nav a{position:absolute;top:13px;font-size:11px;color:var(--white);text-decoration:none;white-space:nowrap;}
.nav a.active{top:8px;left:9px;background:var(--white);color:#333;border-radius:5px;padding:5px 10px;}

.mission{left:83px;top:398px;width:808px;height:219px;background:var(--white);border-radius:8px;box-shadow:0 1px 3px rgba(0,0,0,.15);}
.mission h2{position:absolute;left:17px;top:12px;margin:0;font-family:"Yanone Kaffeesatz",sans-serif;font-size:22px;color:var(--brand-red);text-decoration:underline;letter-spacing:.5px;}
.mission-text{position:absolute;left:17px;top:46px;width:472px;font-size:10.4px;line-height:16.2px;text-align:justify;margin:0;}
.btn{position:absolute;top:184px;height:24px;background:linear-gradient(#1c85b5,var(--button-blue));color:var(--white);font-size:10.5px;font-weight:700;line-height:24px;padding:0 9px;box-sizing:border-box;white-space:nowrap;text-align:center;}
.feature{position:absolute;left:522px;top:38px;width:272px;height:153px;border:2px solid #eee;display:flex;}
.feature-photo{width:150px;height:153px;background:linear-gradient(120deg,#6a4a3a,#c25a2a 55%,#2c2c30);}
.feature-panel{flex:1;background:var(--brand-red);color:var(--white);text-align:right;padding:12px 16px 0 0;font-family:"Yanone Kaffeesatz",sans-serif;font-size:20px;line-height:29px;}

.col h3{margin:0;font-family:"Yanone Kaffeesatz",sans-serif;font-size:22px;color:var(--heading);white-space:nowrap;}
.col-photo{width:182px;height:89px;margin-top:13px;}
.col p{margin:14px 0 0;width:182px;font-size:10px;line-height:16.2px;}
.col .by{font-size:10px;font-weight:700;line-height:18px;color:#333;white-space:nowrap;}
.col .by.navy{color:var(--navy);letter-spacing:.5px;}

.sponsors{left:713px;top:641px;width:178px;height:327px;background:var(--white);border:1px solid #ccc;box-sizing:border-box;}
.badge{position:absolute;left:34px;background:#e9eef2;border-radius:3px;}

.footer{left:0;top:995px;width:974px;height:205px;background:var(--deep-blue);border-top:4px solid #bcd3de;}
.footer h3{position:absolute;margin:0;font-family:"Yanone Kaffeesatz",sans-serif;font-size:25px;color:var(--white);}
.quote{position:absolute;left:100px;top:58px;width:235px;font-size:12px;line-height:18px;color:var(--white);margin:0;}
.links{position:absolute;left:384px;top:58px;margin:0;padding:0;list-style:none;}
.links li{font-size:12px;color:var(--white);line-height:22.7px;padding-left:18px;position:relative;white-space:nowrap;}
.links li::before{content:"";position:absolute;left:1px;top:9px;width:5px;height:5px;border-radius:50%;background:#c9dbe4;}
.foot-logo{position:absolute;left:652px;top:50px;display:flex;align-items:center;gap:8px;font-weight:700;font-size:40px;color:var(--white);}
.foot-logo .logo-dot{background:var(--white);width:18px;height:18px;}
.copy{position:absolute;left:650px;top:165px;font-size:9.5px;color:var(--white);white-space:nowrap;}
</style>
</head>
<body>
<div class="page">
  <div class="abs hero" role="img" aria-label="Welder in a protective helmet with sparks flying"></div>
  <h1 class="abs hero-title">Trésmiðjufélag Kjalar</h1>
  <p class="abs hero-sub">Lorem ipsum dolor sit amet, consectetur adipiscing elit,</p>

  <div class="abs header"></div>
  <div class="abs logo"><span class="logo-dot"></span>TKBÓ</div>
  <div class="abs call">
    <svg width="24" height="24" viewBox="0 0 24 24"><circle cx="12" cy="12" r="11" fill="#d42b2f"/><path d="M8 7c1 4 4 8 8 10l1.5-1.5-2-2-1.5 1c-1.5-1-3-2.5-4-4l1-1.5-2-2z" fill="#fff"/></svg>
    Call +006155501420
  </div>
  <div class="abs search"><div class="search-field">Choose One</div><div class="search-go">GO</div></div>
  <nav class="abs nav">
    <a class="active" href="#">HOME</a>
    <a href="#" style="left:91px">NEWS</a>
    <a href="#" style="left:162px">EDUCATION</a>
    <a href="#" style="left:265px">LIBRARY</a>
    <a href="#" style="left:347px">LOKALAVD</a>
    <a href="#" style="left:442px">YOUNG STUD</a>
  </nav>

  <section class="abs mission">
    <h2>MISSION TKBÓ</h2>
    <p class="mission-text">Lorem ipsum dolor sit amet, consectetur adipiscing elit, sed do eiusmod tempor incididunt ut labore et dolore magna aliqua. Ut enim ad minim veniam, quis nostrud exercitation ullamco laboris nisi ut aliquip ex ea commodo consequat. Duis aute irure dolor in reprehenderit in voluptate velit esse cillum dolore eu fugiat nulla pariatur.<br><br>Excepteur sint occaecat cupidatat non proident, sunt in culpa qui officia deserunt doloremque laudantium Sed ut perspiciatis unde omnis iste natus error sit voluptatem accusantium..</p>
    <div class="btn" style="left:16px;width:155px">Board of Directors Profile</div>
    <div class="btn" style="left:182px;width:275px;padding:0 4px">Extract of 101 Mission Statements (Featuring OE)</div>
    <div class="feature">
      <div class="feature-photo" role="img" aria-label="Welder working on metal with sparks"></div>
      <div class="feature-panel">Welding<br>&amp; Metal<br>working<br>industry</div>
    </div>
  </section>

  <div class="abs col" style="left:98px;top:638px">
    <h3>Customer focus</h3>
    <div class="col-photo" role="img" aria-label="Welder at work in a workshop" style="background:linear-gradient(135deg,#1c2a44,#4c6c9c 45%,#d08a2a 70%,#2a2a2a)"></div>
    <p style="text-align:justify">"On behalf of Halvard Medical [USA], I want to thank you for the efforts of your staff... Your efforts required the cooperation of many people and processes... You all sat down, worked out the logistics and issues to get us our parts....</p>
    <div class="by navy" style="margin-top:6px">The Purchasing Manager<br>Halvard Medical [USA]</div>
  </div>
  <div class="abs col" style="left:303px;top:638px">
    <h3>TKBÓ Workers</h3>
    <div class="col-photo" role="img" aria-label="Welder on a steel beam against blue sky" style="background:linear-gradient(180deg,#1e88d8,#4aa3e6 60%,#5a4a3a)"></div>
    <p>A “Jewel in the crown of British Engineering”, TKBÓ Engineering combines a wealth of experience with the highest integrity.</p>
    <div class="by" style="margin-top:58px">The Secretary of State for Trade<br>and Industry</div>
  </div>
  <div class="abs col" style="left:505px;top:638px">
    <h3>Strategic relationship</h3>
    <div class="col-photo" role="img" aria-label="Welder silhouetted against a sunset" style="background:linear-gradient(180deg,#e0402a,#f0a030 55%,#3a1a14)"></div>
    <p>“TKBÓ Engineering is the most proactive and strategic mechanical supplier. The relationship example is used as a benchmark to all suppliers.”</p>
    <div class="by" style="margin-top:58px;padding-left:3px">One of the world’s largest electrical<br>engineering and electronics.</div>
  </div>

  <aside class="abs sponsors" aria-label="Partner advertisements">
    <div class="badge" style="top:28px;width:110px;height:52px"></div>
    <div class="badge" style="top:94px;width:100px;height:28px"></div>
    <div class="badge" style="top:136px;width:100px;height:40px"></div>
    <div class="badge" style="top:190px;width:100px;height:52px"></div>
    <div class="badge" style="top:248px;width:110px;height:52px"></div>
  </aside>

  <footer class="abs footer">
    <h3 style="left:81px;top:20px">Testimonials</h3>
    <svg style="position:absolute;left:81px;top:58px" width="16" height="14" viewBox="0 0 16 14"><path d="M0 14V8C0 3 2 1 6 0v3C4 4 3 5 3 7h3v7zM9 14V8c0-5 2-7 6-8v3c-2 1-3 2-3 4h3v7z" fill="#9bb8c6"/></svg>
    <p class="quote">Video ads are free to create. Only pay to remove the watermark and download in high resolution when you're 100% satisfied with your ad. Once you've bought your ad, use it in the following places to increase sales and conversions <svg width="16" height="14" viewBox="0 0 16 14"><path d="M16 0v6c0 5-2 7-6 8v-3c2-1 3-2 3-4h-3V0zM7 0v6c0 5-2 7-6 8v-3c2-1 3-2 3-4H1V0z" fill="#9bb8c6"/></svg></p>
    <h3 style="left:381px;top:20px">Quick Links</h3>
    <ul class="links">
      <li>HOME</li><li>ABOUT US</li><li>PROPERTIES</li><li>SERVICES &amp; NEWS</li><li>REFERENCES</li><li>CONTACT</li>
    </ul>
    <div class="foot-logo"><span class="logo-dot"></span>TKBÓ</div>
    <div class="copy">© 2014 TKBÓ, ALL RIGHTS RESERVED.</div>
  </footer>
</div>
</body>
</html>
```